Main Banner for Hullwrap.com, SIMPLE REDESIGN

We need to redesign the main banner that appears on the homepage of our website.

Attached in the project brief is a reference.

There are alot of things we like that we want to keep from that concept but its overall just something I drew on paint and not designed well.

1. Keep yellow tabs on the right hand side, we want them bigger and bolder and to showcase the bullet points inside.
2. Get rid of the 10 yr warranty emblem and replace that with our Brandell logo also attached to the brief.
3. Keep the bottom header and include hullwrap.com and the phone number, but make it look bolder and nicer.
4. Keep the watermark

Aside from these points what we really need is this but a better cleaner more professional version of it.

Target Market(s)

Visitors to our website hullwrap.com we want this banner to include all the major selling points, branding of the product and info on how to contact us.

Requirements
Must have
• Must be clean and professional. My fear is getting submissions that are too busy or messy. There are a lot of components but the challenge is to put them all in there in a clean professional way.
Should not have
• An image in the background like a beach or some kind of picture want the focus to be the requirements listed in the project description

```html
<!DOCTYPE html>
<html lang="en">
<head>
<meta charset="utf-8">
<title>Brandell Summit Boat Cover — Hullwrap.com</title>
<link rel="stylesheet" href="https://fonts.googleapis.com/css2?family=Roboto+Condensed:wght@700;800&family=Roboto:wght@700;900&display=swap">
<style>
  :root {
    --navy: #1d3452;
    --navy-deep: #142740;
    --cover-blue: #27406b;
    --hull-grey: #c9ced6;
    --yellow: #f7c318;
    --star: #f5c842;
    --bg-top: #ffffff;
    --bg-bottom: #eef1f5;
    --ink: #1b2b44;
  }
  * { margin: 0; padding: 0; box-sizing: border-box; }
  html, body { width: 1200px; height: 689px; overflow: hidden; background: #ffffff; }
  .banner {
    position: relative;
    width: 1200px;
    height: 689px;
    overflow: hidden;
    background: linear-gradient(180deg, var(--bg-top) 0%, var(--bg-bottom) 100%);
    font-family: "Roboto", sans-serif;
    color: var(--ink);
  }
  .brand-mark {
    position: absolute;
    left: 24px;
    top: 16px;
    width: 122px;
    height: 122px;
    display: flex;
    flex-direction: column;
    align-items: center;
    justify-content: center;
    gap: 8px;
  }
  .brand-mark .square {
    width: 62px;
    height: 62px;
    background: var(--navy);
  }
  .brand-mark .name {
    font-family: "Roboto Condensed", sans-serif;
    font-weight: 700;
    font-size: 24px;
    color: var(--navy);
    letter-spacing: 1px;
  }
  .headline {
    position: absolute;
    left: 164px;
    top: 52px;
    width: 1012px;
    font-family: "Roboto Condensed", sans-serif;
    font-weight: 800;
    font-size: 68px;
    line-height: 1;
    letter-spacing: 1px;
    color: var(--navy);
    white-space: nowrap;
    text-align: center;
  }
  .rating {
    position: absolute;
    left: 446px;
    top: 132px;
    display: flex;
    gap: 10px;
  }
  .rating svg { width: 52px; height: 50px; }
  .product-visual {
    position: absolute;
    left: 34px;
    top: 186px;
    width: 856px;
    height: 400px;
    border-radius: 48% 52% 40% 44% / 42% 40% 58% 56%;
    background: radial-gradient(ellipse 70% 60% at 50% 40%, var(--cover-blue) 0%, #3b5480 45%, var(--hull-grey) 75%, rgba(238,241,245,0) 100%);
  }
  .selling-points {
    position: absolute;
    right: 0;
    top: 144px;
    display: flex;
    flex-direction: column;
    gap: 8px;
    list-style: none;
  }
  .selling-points li {
    width: 300px;
    height: 52px;
    background: var(--yellow);
    clip-path: polygon(16px 0, 100% 0, 100% 100%, 0 100%);
    display: flex;
    align-items: center;
    padding-left: 34px;
    font-weight: 900;
    font-size: 30px;
    color: var(--navy-deep);
    white-space: nowrap;
  }
  .contact-bar {
    position: absolute;
    left: 0;
    bottom: 0;
    width: 1200px;
    height: 78px;
    background: var(--yellow);
    display: flex;
    align-items: center;
    justify-content: space-between;
    padding: 0 28px 0 34px;
  }
  .contact-bar .site,
  .contact-bar .phone {
    font-weight: 700;
    font-size: 40px;
    color: var(--navy-deep);
  }
</style>
</head>
<body>
  <div class="banner">
    <div class="brand-mark">
      <span class="square"></span>
      <span class="name">Brandell</span>
    </div>

    <h1 class="headline">BRANDELL SUMMIT BOAT COVER</h1>

    <div class="rating" aria-label="Five star rating">
      <svg viewBox="0 0 24 23"><polygon fill="var(--star)" points="12,1 15,8.5 23,9 17,14.5 19,22 12,18 5,22 7,14.5 1,9 9,8.5"/></svg>
      <svg viewBox="0 0 24 23"><polygon fill="var(--star)" points="12,1 15,8.5 23,9 17,14.5 19,22 12,18 5,22 7,14.5 1,9 9,8.5"/></svg>
      <svg viewBox="0 0 24 23"><polygon fill="var(--star)" points="12,1 15,8.5 23,9 17,14.5 19,22 12,18 5,22 7,14.5 1,9 9,8.5"/></svg>
      <svg viewBox="0 0 24 23"><polygon fill="var(--star)" points="12,1 15,8.5 23,9 17,14.5 19,22 12,18 5,22 7,14.5 1,9 9,8.5"/></svg>
      <svg viewBox="0 0 24 23"><polygon fill="var(--star)" points="12,1 15,8.5 23,9 17,14.5 19,22 12,18 5,22 7,14.5 1,9 9,8.5"/></svg>
    </div>

    <div class="product-visual" role="img" aria-label="Boat on a twin-axle trailer wearing a navy fitted cover with tie-down straps"></div>

    <ul class="selling-points">
      <li>10 YR Warranty</li>
      <li>Free Shipping</li>
      <li>Waterproof</li>
    </ul>

    <footer class="contact-bar">
      <span class="site">hullwrap.com</span>
      <span class="phone">call us @ 800-555-0142</span>
    </footer>
  </div>
</body>
</html>
```